Digital Marketing Consultant Needs a Business Card Design

I need a business card to brand myself - I'm a digital marketing consultant, and I do web design, SEO, lead generation, social media, etc. I'm overhauling my website (CorinneDalworth.com) and just had a snazzy new logo made.

I like the combo of yellow & gray - I find it eye-catching, upbeat and techie. The exact colors of yellow and gray that I like are #F6BF27 and #6D6D6D. But I'm open to suggestions and other color combinations!

I plan on printing the card using some high-end printing techniques that will ensure the card stands out - either really thick cards with colored edges, or spot UV. Not sure which yet, so if you want to incorporate that into your design, that'd be great!

I'm looking for a clean and modern design, but something that will really stand out when paired with 'fancy' printing.

Target Market(s)

Small and medium-sized business owners.

Industry/Entity Type

Printing

Contact Information for Business Card

Corinne Dalworth
Digital Marketing
Call or Text: 850-555-0276
Corinne@CorinneDalworth.com
www.CorinneDalworth.com
@QRV58 on Twitter

Font styles to use
Serif
Sans Serif

Requirements
Must have
• My logo, my contact information, and my "company colors" - #F6BF27 and #6D6D6D.
Nice to have
• If there's room to mention all the things that I do:
• Social Media, Web Design, SEO, Lead Generation, Conversion Funnels, PPC
• (don't add if it makes the card cluttered)

```html
<!DOCTYPE html>
<html lang="en">
<head>
<meta charset="utf-8">
<title>Corinne Dalworth – Business Card</title>
<link href="https://fonts.googleapis.com/css2?family=Cinzel:wght@400;500&family=Questrial&display=swap" rel="stylesheet">
<style>
  :root {
    --backdrop: #e4e2df;
    --paper: #f6f6f4;
    --slate: #4b4b4d;
    --slate-mark: #424244;
    --brand-gray: #6d6d6d;
    --brand-yellow: #f6bf27;
    --rule: #b9b9b9;
    --contact-text: #d2d2d2;
  }
  * { box-sizing: border-box; margin: 0; padding: 0; }
  html, body { width: 1200px; height: 1000px; overflow: hidden; }
  body {
    background: var(--backdrop);
    font-family: "Questrial", "Century Gothic", sans-serif;
    position: relative;
  }
  .card {
    position: absolute;
    left: 250px;
    width: 700px;
    height: 400px;
    border-radius: 4px;
    box-shadow: 0 6px 18px rgba(0,0,0,0.12);
    overflow: hidden;
  }
  .card--front { top: 70px; background: var(--paper); }
  .card--back { top: 530px; background: var(--slate); }

  /* Front */
  .brand {
    position: absolute;
    left: 0; right: 0; top: 96px;
    display: flex; flex-direction: column; align-items: center;
  }
  .brand__square {
    width: 62px; height: 62px;
    border: 4px solid var(--brand-gray);
    margin-bottom: 16px;
  }
  .brand__name {
    font-family: "Cinzel", "Trajan Pro", serif;
    font-weight: 400;
    font-size: 38px;
    letter-spacing: 2px;
    color: var(--brand-gray);
    line-height: 1;
  }
  .brand__tagline {
    align-self: flex-end;
    margin-right: 168px;
    margin-top: 4px;
    font-size: 13px;
    letter-spacing: 3px;
    color: var(--brand-gray);
  }
  .brand__rule {
    width: 240px; height: 1px;
    background: var(--rule);
    margin-top: 8px;
    margin-right: 120px;
  }
  .services {
    position: absolute;
    left: 0; right: 0; top: 290px;
    text-align: center;
    font-size: 15px;
    letter-spacing: 1.2px;
    line-height: 1.75;
    color: var(--brand-gray);
  }
  .services .sep { margin: 0 6px; }

  /* Back */
  .back-mark {
    position: absolute;
    right: 90px; top: 70px;
    width: 260px; height: 260px;
    border: 10px solid var(--slate-mark);
  }
  .contacts {
    position: absolute;
    left: 90px; top: 92px;
    list-style: none;
  }
  .contacts li {
    display: flex; align-items: center;
    height: 56px;
    font-size: 20px;
    letter-spacing: 1px;
    color: var(--contact-text);
  }
  .contacts .icon {
    width: 22px; height: 22px;
    margin-right: 24px;
    flex: none;
  }
</style>
</head>
<body>

<section class="card card--front" aria-label="Business card front">
  <div class="brand">
    <div class="brand__square"></div>
    <div class="brand__name">CORINNE DALWORTH</div>
    <div class="brand__tagline">digital marketing</div>
    <div class="brand__rule"></div>
  </div>
  <p class="services">
    Web Design<span class="sep">|</span>Lead Generation<span class="sep">|</span>SEO<br>
    PPC<span class="sep">|</span>Social Media<span class="sep">|</span>Conversion Funnels
  </p>
</section>

<section class="card card--back" aria-label="Business card back">
  <div class="back-mark" aria-hidden="true"></div>
  <ul class="contacts">
    <li>
      <svg class="icon" viewBox="0 0 22 22" aria-hidden="true">
        <circle cx="11" cy="11" r="9" fill="none" stroke="#f6bf27" stroke-width="2"/>
        <ellipse cx="11" cy="11" rx="4" ry="9" fill="none" stroke="#f6bf27" stroke-width="1.6"/>
        <line x1="2" y1="11" x2="20" y2="11" stroke="#f6bf27" stroke-width="1.6"/>
      </svg>
      www.CorinneDalworth.com
    </li>
    <li>
      <svg class="icon" viewBox="0 0 22 22" aria-hidden="true">
        <circle cx="11" cy="11" r="9" fill="none" stroke="#f6bf27" stroke-width="2"/>
        <circle cx="11" cy="11" r="3.5" fill="none" stroke="#f6bf27" stroke-width="2"/>
      </svg>
      Corinne@CorinneDalworth.com
    </li>
    <li>
      <svg class="icon" viewBox="0 0 22 22" aria-hidden="true">
        <rect x="6" y="2" width="10" height="18" rx="2" fill="none" stroke="#f6bf27" stroke-width="2"/>
        <line x1="10" y1="17" x2="12" y2="17" stroke="#f6bf27" stroke-width="1.6"/>
      </svg>
      850-555-0276
    </li>
    <li>
      <svg class="icon" viewBox="0 0 22 22" aria-hidden="true">
        <circle cx="11" cy="11" r="9" fill="#f6bf27"/>
      </svg>
      @QRV58
    </li>
  </ul>
</section>

</body>
</html>
```